Letterhead and Comps Slip Design Project

Letterhead and Compliments Slip for our company in line with our branding in particular our current business card design. 'AdBloom' is and advertising sales specialist. We want the stationary to incorporate our logo and the colour blue.

Our business card design used blue well and the designer also created a subtle watermark effect with our logo on the front that I think could also be used in the design.

Target Market(s)

Business to business sales - professional look important

Industry/Entity Type

Advertising

Requirements
Must have
• Logo (uploaded), similar look/feel to business card design(uploaded), use of blue and watermark effect.

These details:
AdBloom Pty Ltd
ABN 82 604 317 925

Office
The Waypoint
Suite 4&5, 41-57 Garrow St
Surry Hills
NSW 2010

Phone
1300 486 253

International
+61 2 7341 2908

Fax
+61 2 6208 3196

Email
info@adbloom.example.au

Web
www.adbloom.example.au

```html
<!DOCTYPE html>
<html lang="en">
<head>
<meta charset="utf-8">
<title>AdBloom Stationery</title>
<link href="https://fonts.googleapis.com/css2?family=Arimo:wght@400;700&display=swap" rel="stylesheet">
<style>
  :root {
    --backdrop: #e9eaeb;
    --paper: #ffffff;
    --navy: #0b3a7a;
    --sky: #27b8f0;
    --orange: #f47a1f;
    --ink: #2b2b2b;
    --grey-text: #6b6b6b;
    --mark: #1f7fd0;
    --wm-fill: rgba(39, 150, 230, 0.09);
    --wm-edge: rgba(39, 150, 230, 0.02);
    --wm-text: rgba(31, 127, 208, 0.08);
  }
  * { box-sizing: border-box; margin: 0; padding: 0; }
  html, body { width: 1200px; height: 900px; overflow: hidden; }
  body {
    background: var(--backdrop);
    font-family: "Arimo", Arial, sans-serif;
    color: var(--ink);
    position: relative;
  }
  .sheet {
    position: absolute;
    background: var(--paper);
    overflow: hidden;
    box-shadow: 0 2px 6px rgba(0, 0, 0, 0.12);
  }
  .brand {
    display: flex;
    align-items: center;
    gap: 8px;
    color: var(--mark);
    font-weight: 700;
    white-space: nowrap;
    line-height: 1;
  }
  .brand-dot {
    border-radius: 50%;
    background: var(--mark);
    flex: none;
  }

  /* Faint brand decoration: one plain circle plus the name */
  .watermark {
    position: absolute;
    display: flex;
    flex-direction: column;
    align-items: center;
    pointer-events: none;
  }
  .watermark-circle {
    border-radius: 50%;
    background: radial-gradient(circle at 50% 45%, var(--wm-fill) 0%, var(--wm-fill) 55%, var(--wm-edge) 100%);
  }
  .watermark-name {
    color: var(--wm-text);
    font-weight: 700;
    white-space: nowrap;
    line-height: 1;
  }

  .band {
    position: absolute;
    left: 0; right: 0; bottom: 0;
    background: linear-gradient(90deg, var(--navy) 0%, #1565b8 22%, var(--sky) 45%, var(--sky) 70%, #1565b8 88%, var(--navy) 100%);
    overflow: hidden;
  }
  .band-stripe {
    position: absolute;
    top: -4px; bottom: -4px;
    width: 5px;
    background: var(--orange);
    box-shadow: 5px 0 0 #ffffff;
    transform: skewX(-35deg);
  }

  /* Letterhead */
  .letterhead { left: 42px; top: 132px; width: 438px; height: 619px; }
  .letterhead > .brand { position: absolute; top: 24px; left: 50%; transform: translateX(-50%); font-size: 20px; }
  .letterhead > .brand .brand-dot { width: 34px; height: 34px; }
  .letterhead .watermark { left: 50%; top: 176px; transform: translateX(-50%); gap: 14px; }
  .letterhead .watermark-circle { width: 230px; height: 230px; }
  .letterhead .watermark-name { font-size: 44px; }
  .letterhead-address {
    position: absolute; left: 0; right: 0; bottom: 16px;
    text-align: center; font-size: 6.5px; font-weight: 700; color: var(--ink);
  }
  .letterhead .band { height: 11px; display: flex; align-items: center; font-size: 5.5px; color: #fff; font-weight: 700; }
  .letterhead .band-stripe { left: 128px; }
  .letterhead-web { position: absolute; left: 30px; }
  .letterhead-contacts { position: absolute; left: 150px; display: flex; gap: 6px; }
  .letterhead-contacts .sep { opacity: 0.7; }

  /* Envelope back */
  .envelope-back { left: 540px; top: 132px; width: 503px; height: 218px; }
  .envelope-flap { position: absolute; left: 0; top: 0; width: 503px; height: 62px; }
  .envelope-back .brand { position: absolute; top: 12px; left: 50%; transform: translateX(-50%); font-size: 14px; gap: 6px; }
  .envelope-back .brand-dot { width: 28px; height: 28px; }
  .envelope-back .band { top: 54px; bottom: auto; height: 6px; left: 15px; right: 15px; }
  .envelope-back .band-stripe { left: 150px; width: 3px; box-shadow: 3px 0 0 #fff; }

  /* Envelope front */
  .envelope-front { left: 657px; top: 230px; width: 503px; height: 219px; }
  .envelope-front > .brand { position: absolute; top: 58px; left: 36px; font-size: 20px; }
  .envelope-front > .brand .brand-dot { width: 34px; height: 34px; }
  .envelope-front .watermark { right: 44px; top: 22px; gap: 8px; }
  .envelope-front .watermark-circle { width: 118px; height: 118px; }
  .envelope-front .watermark-name { font-size: 22px; }
  .envelope-address { position: absolute; left: 48px; top: 142px; font-size: 11px; line-height: 12px; font-style: normal; }
  .envelope-web { position: absolute; left: 48px; top: 190px; font-size: 10px; color: var(--grey-text); }
  .envelope-front .band { height: 10px; }
  .envelope-front .band-stripe { left: 155px; }

  /* Business cards */
  .card { top: 577px; width: 188px; height: 105px; border-radius: 6px; }
  .card-front { left: 614px; }
  .card-back { left: 823px; }
  .card-front .watermark { left: 112px; top: 6px; gap: 3px; }
  .card-front .watermark-circle { width: 58px; height: 58px; }
  .card-front .watermark-name { font-size: 10px; }
  .card-front > .brand { position: absolute; top: 36px; left: 94px; font-size: 12px; gap: 4px; }
  .card-front > .brand .brand-dot { width: 18px; height: 18px; }
  .card-details { position: absolute; left: 10px; top: 47px; font-size: 4.6px; font-weight: 700; line-height: 5.8px; list-style: none; }
  .card-front .band { height: 8px; }
  .card-front .band-stripe { left: 72px; width: 3px; box-shadow: 3px 0 0 #fff; }
  .card-back .brand { position: absolute; top: 26px; left: 50%; transform: translateX(-50%); font-size: 13px; gap: 5px; }
  .card-back .brand-dot { width: 28px; height: 28px; }
  .card-back-web { position: absolute; left: 0; right: 0; top: 78px; text-align: center; font-size: 8px; color: var(--ink); }
</style>
</head>
<body>

  <section class="sheet letterhead" aria-label="Letterhead">
    <div class="watermark" aria-hidden="true">
      <span class="watermark-circle"></span>
      <span class="watermark-name">AdBloom</span>
    </div>
    <div class="brand"><span class="brand-dot"></span>AdBloom</div>
    <p class="letterhead-address">The Waypoint, Suite 4&amp;5, 41-57 Garrow St, Surry Hills, NSW 2010</p>
    <div class="band">
      <span class="band-stripe"></span>
      <span class="letterhead-web">www.adbloom.example.au</span>
      <span class="letterhead-contacts">
        <span>1300 486 253</span><span class="sep">|</span>
        <span>+61 2 7341 2908</span><span class="sep">|</span>
        <span>+61 2 6208 3196</span><span class="sep">|</span>
        <span>info@adbloom.example.au</span>
      </span>
    </div>
  </section>

  <section class="sheet envelope-back" aria-label="Envelope back">
    <svg class="envelope-flap" viewBox="0 0 503 62" aria-hidden="true">
      <defs>
        <linearGradient id="flap-shade" x1="0" y1="0" x2="0" y2="1">
          <stop offset="0" stop-color="#ffffff"/>
          <stop offset="1" stop-color="#f4f5f6"/>
        </linearGradient>
      </defs>
      <polygon points="0,0 503,0 488,60 15,60" fill="url(#flap-shade)" stroke="#d9dadc" stroke-width="1"/>
    </svg>
    <div class="brand"><span class="brand-dot"></span>AdBloom</div>
    <div class="band"><span class="band-stripe"></span></div>
  </section>

  <section class="sheet envelope-front" aria-label="Envelope front">
    <div class="watermark" aria-hidden="true">
      <span class="watermark-circle"></span>
      <span class="watermark-name">AdBloom</span>
    </div>
    <div class="brand"><span class="brand-dot"></span>AdBloom</div>
    <address class="envelope-address">
      The Waypoint<br>
      Suite 4&amp;5, 41-57 Garrow St<br>
      Surry Hills, NSW 2010
    </address>
    <p class="envelope-web">www.adbloom.example.au</p>
    <div class="band"><span class="band-stripe"></span></div>
  </section>

  <section class="sheet card card-front" aria-label="Business card front">
    <div class="watermark" aria-hidden="true">
      <span class="watermark-circle"></span>
    </div>
    <div class="brand"><span class="brand-dot"></span>AdBloom</div>
    <ul class="card-details">
      <li>The Waypoint</li>
      <li>Suite 4&amp;5, 41-57 Garrow St</li>
      <li>Surry Hills, NSW 2010</li>
      <li>1300 486 253</li>
      <li>+61 2 7341 2908</li>
      <li>+61 2 6208 3196</li>
      <li>info@adbloom.example.au</li>
      <li>www.adbloom.example.au</li>
    </ul>
    <div class="band"><span class="band-stripe"></span></div>
  </section>

  <section class="sheet card card-back" aria-label="Business card back">
    <div class="brand"><span class="brand-dot"></span>AdBloom</div>
    <p class="card-back-web">www.adbloom.example.au</p>
  </section>

</body>
</html>
```